Designer Instructions – Updated Referral Program Flyer

(Based on the mock-up in “Brief Layout and Instructions.pdf”)

OVERALL STYLE + LAYOUT

Maintain the same general layout, structure, and flow as the mock-up flyer (front and back).

This is an update of an older flyer, not a full redesign — keep the same sections, proportions, and overall visual feel, but with cleaner, more modern design improvements.

The final flyer should look clean, bold, professional, and high-impact, geared toward realtors, property managers, and contractors who refer work.

FRONT SIDE INSTRUCTIONS
1. Header Section

Remove the Tallow Ridge Builders logo from the top banner.
(Shown on page 1 of the PDF)

2. Main Headline

Keep the same three-line structure:
EARN
UNLIMITED
CASH

Center it, maximize impact, and increase the font size of CASH so all three words match in importance.

Make the headline bold, clean, and the main focal point.

3. Cash Incentive Box

Keep the "$500 minimum OR 10% per referral" box, but upgrade the graphics to look sharper and more modern.

Ensure the wording matches exactly what’s in the mock-up.

4. Premier Partner Program Ribbon

Clean up and modernize the "PREMIER PARTNER PROGRAM" bar while keeping the same position and structure.

Ensure the checkmark badge remains crisp and professional.

5. Supporting Icons Section

Keep the four icons/benefit boxes (Guaranteed Payout, Free Evaluations, Affordable Solutions, Industry Leaders) in the same order.

Update the icons to cleaner, more modern styles — but maintain the same meanings.

Improve alignment and spacing for sharper visual consistency.

6. Remove Icons in Contact Area

At the bottom (“CALL TEXT OR BOOK ONLINE 555-014-2796 TallowRidgeBuilders.example”), remove the phone and internet icons, as noted on page 2 of the PDF.

7. Replace All Images

I (Darnell) will provide all updated stock images separately via email.

Replace the flood/water-damage imagery and roof leak with the new images I send.

Keep image placement and proportions the same as the mock-up.

BACK SIDE INSTRUCTIONS
1. Header Image + “REFER / EARN” Section

Maintain the same large split-image layout (“The more you refer, the more you earn”).

Replace all background imagery with the new assets I will send.

Keep the CASH FLOW image section but modernize the type and spacing.

2. “HOW IT WORKS” Section

Preserve the three-column layout:

Refer Flood, Water & Mold Damage

We Take Care of Everything (evaluations/insurance)

Get Paid to Share

Update images, tighten spacing, and use modern iconography.

3. Remove Phone/Internet Icons

Same as the front side — remove small communication icons and keep only the text/number/URL.

4. Bottom Contact Bar

Keep the blue bar, same wording, same layout — just modernize the style if needed for clarity.

5. Replace All Back-Side Images

Again, I will email you the image assets.

Keep the layout EXACT — just update with higher-quality photos and improved design.

TEXT CONTENT (Keep as-is unless spacing adjustments needed)

All text shown in the PDF should remain exactly the same unless spacing or visual balance requires minor adjustments.
Example from page 3:

“REFER FLOOD, MOLD & CONSTRUCTION JOBS”

“We Schedule a Free Estimate. If Approved, You Get Paid.”

“Everybody Benefits From Referrals”

Everything stays, just refreshed and visually improved.

DESIGN GOALS

Flyer should look high-end and trustworthy, not salesy.

Consistent color theme: blues, whites, yellows, same palette as original.

Use bold, modern fonts with strong readability.

Ensure all headlines pop and all benefit boxes are clean, well-aligned, and evenly spaced.

The final result should feel like a premium referral program flyer for a top-tier restoration/remodel company.

FILES I WILL PROVIDE

I will send the designer:

All replacement stock photos

Any updated logos (if needed)

Original high-resolution version of the mock-up (if available)

Any additional icons preferred

0054AA
0677BA
7BADD7
CADEEF
E8F1F8

• Designer Instructions – Updated Referral Program Flyer (Based on the mock-up in “Brief Layout and Instructions.pdf”) OVERALL STYLE + LAYOUT Maintain the same general layout, structure, and flow as the mock-up flyer (front and back). This is an update of an older flyer, not a full redesign — keep the same sections, proportions, and overall visual feel, but with cleaner, more modern design improvements. The final flyer should look clean, bold, professional, and high-impact, geared toward realtors, property managers, and contractors who refer work. FRONT SIDE INSTRUCTIONS 1. Header Section Remove the Tallow Ridge Builders logo from the top banner. (Shown on page 1 of the PDF) 2. Main Headline Keep the same three-line structure: EARN UNLIMITED CASH Center it, maximize impact, and increase the font size of CASH so all three words match in importance. Make the headline bold, clean, and the main focal point. 3. Cash Incentive Box Keep the "$500 minimum OR 10% per referral" box, but upgrade the graphics to look sharper and more modern. Ensure the wording matches exactly what’s in the mock-up. 4. Premier Partner Program Ribbon Clean up and modernize the "PREMIER PARTNER PROGRAM" bar while keeping the same position and structure. Ensure the checkmark badge remains crisp and professional. 5. Supporting Icons Section Keep the four icons/benefit boxes (Guaranteed Payout, Free Evaluations, Affordable Solutions, Industry Leaders) in the same order. Update the icons to cleaner, more modern styles — but maintain the same meanings. Improve alignment and spacing for sharper visual consistency. 6. Remove Icons in Contact Area At the bottom (“CALL TEXT OR BOOK ONLINE 555-014-2796 TallowRidgeBuilders.example”), remove the phone and internet icons, as noted on page 2 of the PDF. 7. Replace All Images I (Darnell) will provide all updated stock images separately via email. Replace the flood/water-damage imagery and roof leak with the new images I send. Keep image placement and proportions the same as the mock-up. BACK SIDE INSTRUCTIONS 1. Header Image + “REFER / EARN” Section Maintain the same large split-image layout (“The more you refer, the more you earn”). Replace all background imagery with the new assets I will send. Keep the CASH FLOW image section but modernize the type and spacing. 2. “HOW IT WORKS” Section Preserve the three-column layout: Refer Flood, Water & Mold Damage We Take Care of Everything (evaluations/insurance) Get Paid to Share Update images, tighten spacing, and use modern iconography. 3. Remove Phone/Internet Icons Same as the front side — remove small communication icons and keep only the text/number/URL. 4. Bottom Contact Bar Keep the blue bar, same wording, same layout — just modernize the style if needed for clarity. 5. Replace All Back-Side Images Again, I will email you the image assets. Keep the layout EXACT — just update with higher-quality photos and improved design. TEXT CONTENT (Keep as-is unless spacing adjustments needed) All text shown in the PDF should remain exactly the same unless spacing or visual balance requires minor adjustments. Example from page 3: “REFER FLOOD, MOLD & CONSTRUCTION JOBS” “We Schedule a Free Estimate. If Approved, You Get Paid.” “Everybody Benefits From Referrals” Everything stays, just refreshed and visually improved. DESIGN GOALS Flyer should look high-end and trustworthy, not salesy. Consistent color theme: blues, whites, yellows, same palette as original. Use bold, modern fonts with strong readability. Ensure all headlines pop and all benefit boxes are clean, well-aligned, and evenly spaced. The final result should feel like a premium referral program flyer for a top-tier restoration/remodel company. FILES I WILL PROVIDE I will send the designer: All replacement stock photos Any updated logos (if needed) Original high-resolution version of the mock-up (if available) Any additional icons preferred

```html
<!DOCTYPE html>
<html lang="en">
<head>
<meta charset="utf-8">
<title>Referral Program Flyer – Tallow Ridge Builders</title>
<link rel="stylesheet" href="https://fonts.googleapis.com/css2?family=Poppins:ital,wght@0,400;0,500;0,600;0,700;0,800;1,400&family=Oswald:wght@500;600;700&display=swap">
<style>
  :root {
    --navy: #1f2d5c;
    --navy-deep: #121c3e;
    --yellow: #f7dc14;
    --gold: #f9c414;
    --orange: #f58a1f;
    --white: #ffffff;
    --ink: #1c2550;
    --water: #b9cfe0;
    --sky: #8fbbe8;
    --paper: #ffffff;
  }
  * { box-sizing: border-box; margin: 0; padding: 0; }
  html, body { width: 1200px; height: 1200px; overflow: hidden; background: var(--paper); }
  body { position: relative; font-family: "Poppins", sans-serif; color: var(--white); }

  .card { position: absolute; left: 206px; width: 796px; height: 514px; background: var(--navy); overflow: hidden; }
  .card--front { top: 67px; }
  .card--back { top: 626px; }

  /* ---------- FRONT ---------- */
  .headline { position: absolute; left: 20px; width: 360px; text-align: center; font-weight: 800; }
  .headline__top { top: 34px; font-size: 35px; letter-spacing: 0.5px; line-height: 1; }
  .headline__cash {
    top: 78px; font-size: 113px; line-height: 1.05; letter-spacing: -1px;
    background: linear-gradient(90deg, var(--yellow) 10%, var(--gold) 50%, var(--orange) 95%);
    -webkit-background-clip: text; background-clip: text; color: transparent;
  }
  .headline__sub { top: 199px; font-size: 22px; font-weight: 700; letter-spacing: 0.2px; }

  .service-seal { position: absolute; left: 33px; top: 263px; width: 92px; height: 92px; }

  .incentive { position: absolute; left: 150px; top: 254px; width: 145px; font-family: "Oswald", sans-serif; }
  .incentive__amount { display: flex; align-items: flex-start; gap: 10px; }
  .incentive__money { display: flex; flex-direction: column; }
  .incentive__money-num { color: var(--yellow); font-size: 38px; font-weight: 600; line-height: 1; }
  .incentive__min { font-family: "Poppins", sans-serif; font-style: italic; font-size: 11px; line-height: 1; margin-top: 1px; padding-left: 3px; color: var(--white); letter-spacing: 0.5px; }
  .incentive__or { font-size: 44px; font-weight: 600; line-height: 1; }
  .incentive__rule { height: 1px; background: var(--white); margin: 5px 0 5px 0; }
  .incentive__pct { display: flex; align-items: center; gap: 6px; }
  .incentive__pct-num { color: var(--yellow); font-size: 40px; font-weight: 600; line-height: 1; }
  .incentive__pct-label { font-family: "Poppins", sans-serif; font-style: italic; font-size: 13px; line-height: 1.35; letter-spacing: 0.5px; }

  .partner-ribbon { position: absolute; left: 314px; top: 266px; width: 80px; text-align: center; font-family: "Oswald", sans-serif; }
  .partner-ribbon__label { color: var(--yellow); font-family: "Poppins", sans-serif; font-weight: 700; font-size: 14px; }
  .partner-ribbon__box { margin-top: 2px; background: var(--white); color: var(--ink); height: 84px; border-radius: 3px; padding-top: 4px; font-weight: 600; font-size: 18px; line-height: 1; }
  .partner-ribbon__tick { display: block; margin: 4px auto 4px; width: 30px; height: 30px; }

  .hero-photo {
    position: absolute; left: 404px; top: 5px; width: 385px; height: 355px;
    border: 2px solid var(--yellow); border-radius: 32px;
    background: linear-gradient(180deg, #dfe6ea 0%, #c9dae6 45%, #8fb2cc 70%, #4d5a66 100%);
  }

  .divider { position: absolute; left: 0; top: 0; }

  .partner-pitch { position: absolute; left: 39px; top: 383px; font-weight: 700; font-size: 24px; line-height: 1.36; }
  .partner-pitch__accent { color: var(--yellow); }

  .contact-tab { position: absolute; left: 0; top: 453px; width: 320px; height: 61px; }
  .contact-tab__shape { position: absolute; inset: 0; }
  .contact-tab__text { position: absolute; left: 40px; top: 4px; color: var(--ink); }
  .contact-tab__label { font-size: 14px; font-weight: 500; letter-spacing: 0.3px; }
  .contact-tab__phone { font-size: 28px; font-weight: 800; line-height: 1.1; letter-spacing: 0.5px; }

  .benefits { position: absolute; left: 335px; top: 392px; width: 460px; display: grid; grid-template-columns: 243px 217px; row-gap: 16px; }
  .benefit { display: flex; gap: 11px; align-items: flex-start; }
  .benefit__icon { flex: none; width: 42px; height: 42px; border-radius: 50%; background: var(--white); margin-top: 4px; display: flex; align-items: center; justify-content: center; }
  .benefit__icon svg { width: 26px; height: 26px; }
  .benefit__title { color: var(--yellow); font-weight: 700; font-size: 13.5px; line-height: 1.3; }
  .benefit__text { font-size: 11px; line-height: 1.2; margin-top: 3px; }

  /* ---------- BACK ---------- */
  .cash-photo {
    position: absolute; left: 330px; top: 0; width: 466px; height: 290px;
    background: linear-gradient(90deg, var(--navy) 0%, #6d7894 25%, #c9ccd6 55%, #dfe1e6 100%);
  }
  .dark-fold { position: absolute; left: 0; top: 0; }
  .refer-headline { position: absolute; left: 97px; top: 34px; width: 174px; height: 230px; }

  .steps-divider { position: absolute; left: 0; top: 0; }

  .step-panel { position: absolute; top: 282px; height: 192px; }
  .step-panel--left { left: 0; width: 274px; background: var(--navy); border-bottom-right-radius: 30px; z-index: 2; }
  .step-panel--mid { left: 250px; width: 300px; background: var(--yellow); z-index: 1; }
  .step-panel--right { left: 524px; width: 272px; background: var(--navy); border-bottom-left-radius: 30px; z-index: 2; }

  .step-photo { position: absolute; top: 271px; height: 116px; border: 2px solid var(--yellow); border-radius: 18px; z-index: 3; }
  .step-photo--drying { left: 11px; width: 249px; background: linear-gradient(180deg, #d9d4cc 0%, #cfd3d6 40%, #3f8fc0 70%, #6e7d86 100%); }
  .step-photo--estimate { left: 274px; width: 248px; border-color: var(--navy); background: linear-gradient(180deg, #a9c3a0 0%, #a6786a 40%, #e7ebef 70%, #6fa7cf 100%); }
  .step-photo--share { left: 536px; width: 248px; background: linear-gradient(160deg, #5b8fd9 0%, var(--sky) 50%, #e9f1fb 100%); }

  .step-caption { position: absolute; top: 394px; width: 250px; text-align: center; z-index: 4; }
  .step-caption--left { left: 11px; }
  .step-caption--mid { left: 273px; color: var(--ink); }
  .step-caption--right { left: 535px; }
  .step-caption__title { font-weight: 800; font-size: 15px; line-height: 1.3; color: var(--yellow); }
  .step-caption--mid .step-caption__title { color: var(--ink); }
  .step-caption--right .step-caption__title { font-weight: 700; font-size: 15.5px; }
  .step-caption__text { font-size: 11px; line-height: 1.3; margin-top: 1px; }

  .contact-bar { position: absolute; left: 0; bottom: 0; width: 796px; height: 40px; background: var(--yellow); color: var(--ink); display: flex; align-items: center; justify-content: space-between; padding: 0 37px; z-index: 5; }
  .contact-bar__phone { font-weight: 800; font-size: 25px; letter-spacing: 0.5px; }
  .contact-bar__web { font-weight: 700; font-size: 17px; }
</style>
</head>
<body>

<section class="card card--front" aria-label="Referral flyer front">
  <div class="hero-photo" role="img" aria-label="Photo of a bright white kitchen with water pouring from a hole in the ceiling onto a blue island"></div>

  <svg class="divider" width="796" height="514" viewBox="0 0 796 514" aria-hidden="true">
    <path d="M0 340 Q0 372 34 372 L770 372 Q796 372 796 345" fill="none" stroke="#ffffff" stroke-width="5"/>
  </svg>

  <h1 class="headline headline__top">EARN UNLIMITED</h1>
  <div class="headline headline__cash">CASH</div>
  <p class="headline headline__sub">GET PAID TOREFER A FLOOD</p>

  <svg class="service-seal" viewBox="0 0 92 92" aria-label="Emergency service seal" role="img">
    <circle cx="46" cy="46" r="45" fill="#ffffff"/>
    <circle cx="46" cy="46" r="38" fill="none" stroke="#c9242b" stroke-width="4"/>
    <circle cx="46" cy="46" r="26" fill="#c9242b"/>
  </svg>

  <div class="incentive">
    <div class="incentive__amount">
      <span class="incentive__money">
        <span class="incentive__money-num">$500</span>
        <span class="incentive__min">MINIMUM</span>
      </span>
      <span class="incentive__or">OR</span>
    </div>
    <div class="incentive__rule"></div>
    <div class="incentive__pct">
      <span class="incentive__pct-num">10%</span>
      <span class="incentive__pct-label">PER<br>REFERRAL</span>
    </div>
  </div>

  <div class="partner-ribbon">
    <div class="partner-ribbon__label">PREMIER</div>
    <div class="partner-ribbon__box">
      PARTNER
      <svg class="partner-ribbon__tick" viewBox="0 0 30 30" aria-hidden="true">
        <circle cx="15" cy="15" r="15" fill="#f7dc14"/>
        <path d="M8 15.5 L13 20 L22 10" fill="none" stroke="#1f2d5c" stroke-width="3.5" stroke-linecap="round" stroke-linejoin="round"/>
      </svg>
      PROGRAM
    </div>
  </div>

  <h2 class="partner-pitch">PARTNER WITH US &amp;<br><span class="partner-pitch__accent">EVERYBODY WINS!</span></h2>

  <div class="contact-tab">
    <svg class="contact-tab__shape" viewBox="0 0 320 61" preserveAspectRatio="none" aria-hidden="true">
      <path d="M0 0 L270 0 Q285 0 292 12 L320 61 L0 61 Z" fill="#f7dc14"/>
    </svg>
    <div class="contact-tab__text">
      <div class="contact-tab__label">CALL TEXT OR BOOK ONLINE</div>
      <div class="contact-tab__phone">555-014-2796</div>
    </div>
  </div>

  <div class="benefits">
    <div class="benefit">
      <span class="benefit__icon"><svg viewBox="0 0 26 26" fill="none" stroke="#1f2d5c" stroke-width="1.6" stroke-linecap="round" stroke-linejoin="round"><path d="M13 2 L15.5 4.5 L19 4 L19.8 7.4 L23 9 L21.8 12.3 L23 15.6 L19.8 17.2 L19 20.6 L15.5 20.1 L13 22.6 L10.5 20.1 L7 20.6 L6.2 17.2 L3 15.6 L4.2 12.3 L3 9 L6.2 7.4 L7 4 L10.5 4.5 Z"/><path d="M9 12.5 L12 15.5 L17 9.5"/></svg></span>
      <div><div class="benefit__title">GUARANTEEDPAYOUT</div><div class="benefit__text">Minimum $500 or 10% of Total<br>Invoice Paid Fast</div></div>
    </div>
    <div class="benefit">
      <span class="benefit__icon"><svg viewBox="0 0 26 26" fill="none" stroke="#1f2d5c" stroke-width="1.6" stroke-linecap="round" stroke-linejoin="round"><rect x="4" y="3" width="12" height="17" rx="1.5"/><path d="M7 8 H13 M7 11 H13 M7 14 H10"/><rect x="13" y="12" width="9" height="11" rx="1.5"/><path d="M15 15 H20 M15 18 H16 M18 18 H20 M15 21 H16 M18 21 H20"/></svg></span>
      <div><div class="benefit__title">FREE ESTIMATES</div><div class="benefit__text">Fast &amp; Free Inspections<br>&amp; Written Estimates</div></div>
    </div>
    <div class="benefit">
      <span class="benefit__icon"><svg viewBox="0 0 26 26" fill="none" stroke="#1f2d5c" stroke-width="1.6" stroke-linecap="round" stroke-linejoin="round"><circle cx="14" cy="9" r="5.5"/><path d="M15.5 6.8 H13 a1.2 1.2 0 0 0 0 2.4 H15 a1.2 1.2 0 0 1 0 2.4 H12.5 M14 5.5 V12.5"/><path d="M3 17 H7 L11 19 H17 a1.5 1.5 0 0 0 0 -3 H12 M7 22 H17 L23 17"/></svg></span>
      <div><div class="benefit__title">AFFORDABLE SOLUTIONS</div><div class="benefit__text">Lowest Out of Pocket Costs for<br>Your Customers</div></div>
    </div>
    <div class="benefit">
      <span class="benefit__icon"><svg viewBox="0 0 26 26" fill="none" stroke="#1f2d5c" stroke-width="1.6" stroke-linecap="round" stroke-linejoin="round"><path d="M13 2 L14 4 L16 4.3 L14.5 5.7 L14.9 7.8 L13 6.8 L11.1 7.8 L11.5 5.7 L10 4.3 L12 4 Z"/><circle cx="13" cy="12" r="2.5"/><circle cx="6.5" cy="14" r="2.2"/><circle cx="19.5" cy="14" r="2.2"/><path d="M9 22 V18.5 a4 4 0 0 1 8 0 V22 M2.5 22 V19.5 a3.5 3.5 0 0 1 5.5 -2.8 M23.5 22 V19.5 a3.5 3.5 0 0 0 -5.5 -2.8"/></svg></span>
      <div><div class="benefit__title">INDUSTRY LEADERS</div><div class="benefit__text">Licensed &amp; Certified Experts<br>Provide 100% Guarantee</div></div>
    </div>
  </div>
</section>

<section class="card card--back" aria-label="Referral flyer back">
  <div class="cash-photo" role="img" aria-label="Photo of hundred dollar bills with letter tiles spelling CASH FLOW, fading into navy on the left"></div>

  <svg class="dark-fold" width="330" height="290" viewBox="0 0 330 290" aria-hidden="true">
    <path d="M0 112 L92 36 L290 36 L290 282 L30 282 Q0 282 0 252 Z" fill="#121c3e"/>
  </svg>

  <svg class="refer-headline" viewBox="0 0 174 230" aria-label="The more you refer, the more you earn" role="img">
    <defs>
      <linearGradient id="earnGlow" x1="0" y1="0" x2="1" y2="0">
        <stop offset="0" stop-color="#f7dc14"/>
        <stop offset="0.55" stop-color="#f9c414"/>
        <stop offset="1" stop-color="#f58a1f"/>
      </linearGradient>
    </defs>
    <g font-family="Oswald, sans-serif" font-weight="700">
      <text x="0" y="32" font-size="36" fill="#ffffff" textLength="174" lengthAdjust="spacingAndGlyphs">THE MORE YOU</text>
      <text x="0" y="106" font-size="82" fill="url(#earnGlow)" textLength="174" lengthAdjust="spacingAndGlyphs">REFER</text>
      <text x="0" y="141" font-size="36" fill="#ffffff" textLength="174" lengthAdjust="spacingAndGlyphs">THE MORE YOU</text>
      <text x="0" y="226" font-size="98" fill="url(#earnGlow)" textLength="174" lengthAdjust="spacingAndGlyphs">EARN</text>
    </g>
  </svg>

  <svg class="steps-divider" width="796" height="300" viewBox="0 0 796 300" aria-hidden="true">
    <path d="M0 252 Q0 283 30 283 L796 283" fill="none" stroke="#ffffff" stroke-width="5"/>
  </svg>

  <div class="step-panel step-panel--mid"></div>
  <div class="step-panel step-panel--left"></div>
  <div class="step-panel step-panel--right"></div>

  <div class="step-photo step-photo--drying" role="img" aria-label="Photo of blue air movers and dehumidifiers drying a basement floor"></div>
  <div class="step-photo step-photo--estimate" role="img" aria-label="Photo of a work estimate on a clipboard in front of a brick house"></div>
  <div class="step-photo step-photo--share" role="img" aria-label="Photo of a yellow road sign reading Get Paid To Share against a blue cloudy sky"></div>

  <div class="step-caption step-caption--left">
    <div class="step-caption__title">REFER FLOOD, MOLD &amp;<br>CONSTRUCTION JOBS:</div>
    <div class="step-caption__text">It’s Simple to Refer 24/7:<br>Call, Text or Book Online.</div>
  </div>
  <div class="step-caption step-caption--mid">
    <div class="step-caption__title">WE TAKE CARE OF<br>EVERYTHING:</div>
    <div class="step-caption__text">We Schedule a Free Estimate.<br>If Approved, You Get Paid.</div>
  </div>
  <div class="step-caption step-caption--right">
    <div class="step-caption__title">Everybody Benefits<br>From Referrals</div>
    <div class="step-caption__text">We Provide Expert Quality<br>Work for Affordable Price.</div>
  </div>

  <div class="contact-bar">
    <span class="contact-bar__phone">555-014-2796</span>
    <span class="contact-bar__web">TallowRidgeBuilders.example</span>
  </div>
</section>

</body>
</html>
```